Bref créative
brochure and folder for a4 brochures
Brush Wave
Protecting your assets
Need a brochure template to use for Strata painting and residential painting
"STRATA BROCHURE COPY"
Brush Wave, the easy choice for strata paint works
Why strata managers love Brush Wave
Work with a company that focuses on your needs – a company that can get your strata painting works done with no hassle. We’ve been in business for over 20 years; we’re your one-stop shop for painting and remedial maintenance, and we get it right the first time.
At Brush Wave, we understand you need:
• Quality painting, project managed by us so you don’t have to take endless phone calls
• Great-value price: We take time to make sure of this
• Great ideas for colour schemes (saving the owners up to $700)
• Remedial repairs overseen by a qualified master builder
Why choose Brush Wave?
The Brush Wave difference means we turn up when we’re supposed to and finish on schedule. All our tradespeople are friendly, professional – and we promise that your site will be cleaner when we’ve finished than when we started.
Once you’ve accepted our quote, we can start within 24 hours and we manage the job from start to finish. You’ll be a hero with owners and you have peace of mind knowing the job’s under control.
Life’s easier with Brush Wave
Take the headache out of your strata painting works. Call Brush Wave on 1300 482 915.
What clients say about us
“Derek and his team have skilfully and professionally painted our property comprising 17 apartments and townhouses. The progress of the work has been clean and efficient and the result is excellent.”
Owen Falkirk, Moorings, Henley
“Communication is the key to successfully managing a project and Derek and his team exceeded expectations with updates concerning all aspects of the work.“ Neil Barker, Randwick
Add value to your new home before you move in, with Brush Wave
"RESIDENTIAL BROCHURE"
Start your new life with a clean freshly painted house
We’ve been in business for over 20 years and we know that when you move into your new home, it’s best to do all the basics first – quickly, with no fuss.
At Brush Wave, we understand you want:
• Quick, clean work: We can start within 24 hours and be in and out before you know it
• Good value: We also make remedial repairs so you get a perfect finish
• Great ideas for colour schemes (saving you up to $700)
• Friendly professional tradies you’ll be happy to have around your home
We turn up when we’re supposed to and finish on time. We’ll quote as soon as you pick up the keys and can advise on colours that will create just the right atmosphere. What’s more, your new home will be cleaner than when we started.
We guarantee
• Great-value price: We’ll help you make sure of this
• Impressive service: Fast, clean, quality job, and responsive to your needs
For feel-good factor, there’s nothing like a fresh splash of colour
If you’d like to start fresh, call Brush Wave on 1300 482 915.
"When dealing with Brush Wave we were given expert and professional advice in choosing colours for our beach house... The end result was great." Fiona Darrowby
Real Estate
corporate FOR STRATA
professional FOR RESIDENTIAL
need one brochure for residential painting and one for strata painting and a folder that we can use for both brochures
please use logo only do not use NSW or website under logo
please see attachment
please only use brushwave not background, lines or website under logo
another log for your use

```html
<!DOCTYPE html>
<html lang="en">
<head>
<meta charset="utf-8">
<title>Brush Wave – Brochures and Presentation Folder</title>
<link rel="stylesheet" href="https://fonts.googleapis.com/css2?family=Open+Sans:wght@400;600;700&display=swap">
<style>
  :root {
    --backdrop: #e9e4dc;
    --navy: #1f3a4d;
    --ink: #3c4650;
    --blue: #2d6fa8;
    --orange: #e0782a;
    --grey-title: #6f7c86;
    --paper: #ffffff;
    --fold-shade: #f3f4f6;
    --room-light: #d9d6d0;
    --room-dark: #5a4032;
    --sky: #9fc0dc;
    --harbour: #2f5f84;
    --accent: #7a3e9d;
  }
  * { box-sizing: border-box; margin: 0; padding: 0; }
  html, body { width: 1200px; height: 1002px; overflow: hidden; }
  body {
    position: relative;
    background: var(--backdrop);
    font-family: "Open Sans", Arial, sans-serif;
    color: var(--ink);
  }
  .sheet { position: absolute; background: var(--paper); box-shadow: 0 2px 6px rgba(0,0,0,.18); overflow: hidden; }

  /* brochure insert page */
  .insert { width: 204px; padding: 0 11px 10px; font-size: 5.6px; line-height: 1.45; }
  .insert h2 { color: var(--blue); font-size: 9px; line-height: 1.2; font-weight: 700; margin: 6px 0 4px; }
  .insert h3 { color: var(--orange); font-size: 6.4px; font-weight: 700; margin: 4px 0 2px; }
  .insert p { margin-bottom: 3px; }
  .insert ul { list-style: none; margin-bottom: 3px; }
  .insert li { padding-left: 7px; position: relative; }
  .insert li::before { content: ""; position: absolute; left: 1px; top: 2.4px; width: 3px; height: 3px; border-radius: 50%; background: var(--blue); }
  .insert .quote { font-style: italic; color: var(--grey-title); }
  .insert-banner { height: 52px; margin: 0 -11px; }
  .insert-head { display: flex; align-items: flex-end; justify-content: space-between; gap: 6px; }
  .insert-head .insert-photo { width: 110px; height: 56px; margin-left: 0; }
  .insert-head .brand { margin-bottom: 4px; }
  .insert-head .brand-name { font-size: 8.5px; }
  .insert-head .brand-dot { width: 6px; height: 6px; }
  .insert-foot-brand { position: absolute; left: 0; right: 0; bottom: 10px; display: flex; justify-content: center; }
  .insert-footer { position: absolute; left: 0; right: 0; bottom: 0; height: 14px; background: var(--navy); color: #fff; font-size: 5px; padding: 3px 8px; white-space: nowrap; }

  /* folder front cover */
  .cover { width: 415px; }
  .cover-photo { position: absolute; inset: 0; }
  .room { background: linear-gradient(90deg, var(--room-light) 0%, #efece7 35%, #f4f2ee 55%, var(--room-dark) 56%, #6b4c3b 100%); }
  .interior { background: linear-gradient(180deg, #e9e6e1 0%, #d8d3cc 60%, #b9b1a7 100%); }
  .city { background: linear-gradient(180deg, var(--sky) 0%, #c9d6df 40%, #8a98a3 58%, var(--harbour) 72%, #24506f 100%); }
  .cover-title { position: absolute; right: 18px; top: 16px; text-align: right; }
  .cover-title h1 { font-size: 13px; font-weight: 600; color: var(--grey-title); }
  .cover-title p { font-size: 8.5px; font-weight: 600; color: var(--orange); margin-top: 2px; }
  .cover .brand { position: absolute; right: 18px; bottom: 14px; }

  /* folder pocket tab */
  .tab { position: absolute; width: 136px; height: 68px; background: var(--navy); border-radius: 0 0 12px 12px; display: flex; align-items: center; justify-content: center; box-shadow: 0 2px 5px rgba(0,0,0,.2); }

  /* folder inside */
  .inside { width: 429px; }
  .inside-fold { position: absolute; top: 0; bottom: 0; left: 214px; right: 0; background: var(--fold-shade); border-left: 1px solid #e1e4e8; }
  .inside-cans { position: absolute; left: 0; top: 0; width: 214px; height: 100%; background: radial-gradient(ellipse at 35% 55%, rgba(190,200,210,.55), rgba(255,255,255,0) 70%); }
  .inside-pocket { position: absolute; right: 0; bottom: 0; width: 203px; height: 60px; background: var(--navy); border-top-left-radius: 10px; display: flex; align-items: center; justify-content: center; }

  /* brand wordmark */
  .brand { display: flex; align-items: center; gap: 4px; white-space: nowrap; }
  .brand-dot { width: 8px; height: 8px; border-radius: 50%; background: var(--accent); flex: none; }
  .brand-name { font-weight: 700; font-size: 11px; color: var(--navy); letter-spacing: .3px; }
  .brand.on-dark .brand-name { color: #fff; }
  .brand.large .brand-name { font-size: 15px; }
  .brand.large .brand-dot { width: 11px; height: 11px; }
</style>
</head>
<body>

<!-- Residential set -->
<article class="sheet insert" style="left:54px; top:103px; height:264px;">
  <div class="insert-banner interior" role="img" aria-label="Bright white living room interior"></div>
  <h2>Start your new life with a clean freshly painted house</h2>
  <p>We've been in business for over 20 years and we know that when you move into your new home, it's best to do all the basics first – quickly, with no fuss.</p>
  <h3>At Brush Wave, we understand you want:</h3>
  <ul>
    <li>Quick, clean work: we can start within 24 hours</li>
    <li>Good value: remedial repairs for a perfect finish</li>
    <li>Great ideas for colour schemes (saving you up to $700)</li>
    <li>Friendly professional tradies</li>
  </ul>
  <h3>We guarantee</h3>
  <ul>
    <li>Great-value price</li>
    <li>Impressive service: fast, clean, quality job</li>
  </ul>
  <p>If you'd like to start fresh, call Brush Wave on 1300 482 915.</p>
  <div class="brand insert-foot-brand"><span class="brand-dot"></span><span class="brand-name">Brush Wave</span></div>
</article>

<section class="sheet cover" style="left:285px; top:103px; height:264px;">
  <div class="cover-photo room" role="img" aria-label="Bright modern living room with white sofa and dark timber feature wall"></div>
  <div class="cover-title">
    <h1>Sydney's Favorite Painting Firm</h1>
    <p>Re-Painting Is What Matters to YOU</p>
  </div>
  <div class="brand"><span class="brand-dot"></span><span class="brand-name">Brush Wave</span></div>
</section>

<div class="tab" style="left:285px; top:367px;">
  <div class="brand on-dark"><span class="brand-dot"></span><span class="brand-name">Brush Wave</span></div>
</div>

<section class="sheet inside" style="left:711px; top:103px; height:264px;">
  <div class="inside-fold"></div>
  <div class="inside-cans" role="img" aria-label="Faded open paint tins in soft colours"></div>
  <div class="inside-pocket">
    <div class="brand on-dark large"><span class="brand-dot"></span><span class="brand-name">Brush Wave</span></div>
  </div>
</section>

<!-- Strata set -->
<article class="sheet insert" style="left:54px; top:557px; height:290px;">
  <div class="insert-head">
    <div class="insert-photo city" role="img" aria-label="City skyline over the harbour"></div>
    <div class="brand"><span class="brand-dot"></span><span class="brand-name">Brush Wave</span></div>
  </div>
  <h2>Why strata managers love Brush Wave</h2>
  <p>Work with a company that focuses on your needs – we get your strata painting works done with no hassle, and right the first time.</p>
  <ul>
    <li>Quality painting, project managed by us</li>
    <li>Great-value price</li>
    <li>Colour scheme ideas (saving owners up to $700)</li>
    <li>Repairs overseen by a qualified master builder</li>
  </ul>
  <h3>Why choose Brush Wave?</h3>
  <p>We turn up when we're supposed to and finish on schedule. Once you've accepted our quote, we can start within 24 hours.</p>
  <p class="quote">"Derek and his team have skilfully and professionally painted our property." – Owen Falkirk, Moorings, Henley</p>
  <div class="insert-footer">Take the headache out of strata painting. Call 1300 482 915.</div>
</article>

<section class="sheet cover" style="left:285px; top:557px; height:290px;">
  <div class="cover-photo city" role="img" aria-label="Aerial view of city towers and harbour with ferries"></div>
  <div class="cover-title">
    <h1>Sydney's Favorite Painting Firm</h1>
    <p>Re-Painting Is What Matters to YOU</p>
  </div>
  <div class="brand on-dark"><span class="brand-dot"></span><span class="brand-name">Brush Wave</span></div>
</section>

<div class="tab" style="left:285px; top:847px;">
  <div class="brand on-dark"><span class="brand-dot"></span><span class="brand-name">Brush Wave</span></div>
</div>

<section class="sheet inside" style="left:711px; top:557px; height:290px;">
  <div class="inside-fold"></div>
  <div class="inside-cans" role="img" aria-label="Faded open paint tins in soft colours"></div>
  <div class="inside-pocket">
    <div class="brand on-dark large"><span class="brand-dot"></span><span class="brand-name">Brush Wave</span></div>
  </div>
</section>

</body>
</html>
```